PowerPoint template for online medical education

Need a PowerPoint design for our online urgent care education content Need a title page and then further pages.

must have our logo, name and tagline Academy of Rapid Clinical Practice
Elevating Care, Shaping the Field
Should match our logo colors scheme

enclosed our logo, tagline ans a copy of our newsletter

Target Market(s)

PHYSICIANS, and other professionals

Industry/Entity Type

Medicine

Font styles to use
Serif

Requirements
Must have
• our logo
• tagline
• color scheme like our logo
Should not have
• too much on content pages

```html
<!DOCTYPE html>
<html lang="en">
<head>
<meta charset="utf-8">
<title>Academy of Rapid Clinical Practice – Presentation Template</title>
<link href="https://fonts.googleapis.com/css2?family=Oswald:wght@300;500;600&family=Montserrat:wght@400;500;600&family=Libre+Baskerville:ital@1&display=swap" rel="stylesheet">
<style>
  :root {
    --board: #b9b9b9;
    --paper: #ffffff;
    --orange: #c9531f;
    --orange-deep: #7a2e0f;
    --tab: #eea534;
    --title-red: #b7321d;
    --ink: #1d1d1d;
    --body: #4a4a4a;
    --muted: #7d7d7d;
    --avatar: #d9d9d9;
  }
  * { margin: 0; padding: 0; box-sizing: border-box; }
  html, body { width: 1200px; height: 915px; overflow: hidden; background: var(--board); }
  .board { position: relative; width: 1200px; height: 915px; }

  .board-label {
    position: absolute; width: 543px; text-align: center;
    font-family: "Oswald", sans-serif; font-weight: 500; font-size: 40px;
    color: var(--ink); letter-spacing: -0.5px; line-height: 1;
  }

  .slide {
    position: absolute; width: 543px; height: 304px; background: var(--paper);
    overflow: hidden; box-shadow: 0 18px 14px -12px rgba(0,0,0,0.45);
    font-family: "Montserrat", sans-serif;
  }
  .slide--cover { left: 48px; top: 120px; }
  .slide--fellowship { left: 617px; top: 120px; }
  .slide--team { left: 48px; top: 501px; }
  .slide--membership { left: 617px; top: 501px; }

  .brand { position: absolute; display: flex; align-items: center; gap: 6px; }
  .brand__dot { width: 14px; height: 14px; border-radius: 50%; background: var(--orange); flex: none; }
  .brand__name {
    font-family: "Montserrat", sans-serif; font-weight: 400; color: var(--muted);
    text-transform: uppercase; letter-spacing: 0.5px; line-height: 1.15;
    border-left: 1px solid #c9c9c9; padding-left: 6px;
  }
  .brand--cover .brand__dot { width: 22px; height: 22px; }
  .brand--cover .brand__name { font-size: 8.5px; }
  .brand--footer .brand__name { font-size: 5.4px; }

  .cover-photo {
    position: absolute; left: 0; top: 0; width: 543px; height: 212px;
    background: linear-gradient(90deg, #9a9a9a 0%, #6d6d6d 35%, #4d4d4d 55%, #3a2014 70%, #5a240e 100%);
  }
  .cover-overlay { position: absolute; left: 0; top: 0; }
  .cover-title {
    position: absolute; left: 294px; top: 94px; color: #fff;
    font-family: "Oswald", sans-serif; line-height: 1.1;
  }
  .cover-title__light { display: block; font-weight: 300; font-size: 26px; letter-spacing: 0.3px; }
  .cover-title__bold { display: block; font-weight: 600; font-size: 28px; letter-spacing: 0.5px; }
  .cover-tagline {
    position: absolute; left: 309px; top: 279px;
    font-family: "Libre Baskerville", serif; font-style: italic; font-size: 5.6px; color: var(--title-red);
  }

  .page-tab { position: absolute; left: 0; top: 16px; }
  .page-tab__num {
    position: absolute; left: 0; top: 16px; width: 45px; height: 14px; line-height: 14px;
    text-align: center; font-size: 8px; color: #fff; font-weight: 500;
  }
  .footer-band { position: absolute; left: 0; bottom: 0; }
  .footer-url {
    position: absolute; right: 16px; bottom: 4px; font-size: 7.5px; color: #fff;
    letter-spacing: 0.3px;
  }
  .brand--footer { left: 16px; bottom: 10px; }

  .slide-title {
    position: absolute; left: 0; top: 12px; width: 543px; text-align: center;
    font-family: "Oswald", sans-serif; font-weight: 500; font-size: 21px;
    color: var(--title-red); letter-spacing: -0.2px; line-height: 1.2;
  }
  .slide-title__tag { font-weight: 300; }

  .lead {
    position: absolute; left: 14px; top: 56px; width: 513px;
    font-size: 7.6px; line-height: 1.36; color: var(--body); text-align: justify; letter-spacing: 0.2px;
  }
  .feature-image {
    position: absolute; left: 14px; top: 128px; width: 513px; height: 120px;
    background: radial-gradient(ellipse at 70% 50%, #a8864c 0%, #5b4a33 30%, #2b2620 65%, #1a1816 100%);
  }

  .team { position: absolute; left: 14px; top: 68px; width: 515px; display: flex; justify-content: space-between; }
  .member { width: 96px; text-align: center; }
  .member__photo {
    width: 76px; height: 76px; margin: 0 auto; border-radius: 50%;
    background: var(--avatar); border: 3px solid #fff; box-shadow: 0 0 0 1.5px #cfcfcf;
  }
  .member__name { margin-top: 7px; font-size: 8.5px; font-weight: 600; color: var(--title-red); }
  .member__bio {
    margin-top: 2px; font-size: 5.6px; line-height: 1.45; color: var(--body);
    text-align: justify; text-align-last: center; hyphens: auto; -webkit-hyphens: auto;
  }

  .member-types { position: absolute; left: 15px; top: 44px; width: 375px; }
  .member-type + .member-type { margin-top: 6px; }
  .member-type__head {
    display: flex; align-items: center; gap: 4px;
    font-family: "Oswald", sans-serif; font-weight: 500; font-size: 9px; color: var(--title-red);
  }
  .member-type__head svg { flex: none; }
  .member-type__text { margin-top: 3px; font-size: 5.6px; line-height: 1.5; color: var(--body); text-align: justify; }
  .membership-photo {
    position: absolute; left: 402px; top: 14px; width: 128px; height: 260px;
    background: linear-gradient(180deg, #c9ad76 0%, #b59a66 40%, #7e6a4d 75%, #5b4b39 100%);
  }
</style>
</head>
<body>
<main class="board">

  <p class="board-label" style="left:48px; top:60px;">COVER</p>
  <p class="board-label" style="left:617px; top:60px;">INSIDE PAGE-1</p>
  <p class="board-label" style="left:48px; top:830px;">INSIDE PAGE-2</p>
  <p class="board-label" style="left:617px; top:830px;">INSIDE PAGE-3</p>

  <section class="slide slide--cover">
    <div class="cover-photo" role="img" aria-label="Black and white photo of a scientist holding a flask in front of a periodic table chalkboard"></div>
    <svg class="cover-overlay" width="543" height="226" viewBox="0 0 543 226" aria-hidden="true">
      <polygon points="316,0 543,0 543,212 242,212" fill="#c9531f" opacity="0.55"/>
      <polygon points="242,212 543,212 543,226 240,226" fill="#c9531f"/>
    </svg>
    <h1 class="cover-title">
      <span class="cover-title__light">ACADEMY OF RAPID</span>
      <span class="cover-title__bold">CLINICAL PRACTICE</span>
    </h1>
    <div class="brand brand--cover" style="left:130px; top:242px;">
      <span class="brand__dot"></span>
      <span class="brand__name">Academy of<br>Rapid Clinical<br>Practice</span>
    </div>
    <p class="cover-tagline">Elevating Care, Shaping the Field</p>
  </section>

  <section class="slide slide--fellowship">
    <svg class="page-tab" width="56" height="14" viewBox="0 0 56 14" aria-hidden="true"><polygon points="0,0 56,0 48,14 0,14" fill="#eea534"/><polygon points="48,14 56,0 54,0 46,14" fill="#c9531f"/></svg>
    <span class="page-tab__num">1</span>
    <h2 class="slide-title">DEGREE OF FELLOWSHIP <span class="slide-title__tag">(FARCP)</span></h2>
    <p class="lead">Our fellowship in the academy is now open to all physician members. Fellowship in the Academy denotes dedication to the specialty and pursuing excellence. Criteria can be found on the application here. The link will take you to ARN website. They administer this for us. Until the end of 2017 the need for recommendation from a current fellow will be waived. Each year fellows are invited to receive their certificates in a formal manner during the Rapid Care Foundation Celebration or our membership meeting at the Fall Conference. If you have question feel free to email us info@arcp-academy.org</p>
    <div class="feature-image" role="img" aria-label="Close-up illustration of a glowing DNA double helix"></div>
    <svg class="footer-band" width="543" height="18" viewBox="0 0 543 18" aria-hidden="true"><polygon points="104,0 543,0 543,18 94,18" fill="#c9531f"/></svg>
    <div class="brand brand--footer"><span class="brand__dot"></span><span class="brand__name">Academy of<br>Rapid Clinical<br>Practice</span></div>
    <span class="footer-url">www.arcp-academy.org</span>
  </section>

  <section class="slide slide--team">
    <svg class="page-tab" width="56" height="14" viewBox="0 0 56 14" aria-hidden="true"><polygon points="0,0 56,0 48,14 0,14" fill="#eea534"/><polygon points="48,14 56,0 54,0 46,14" fill="#c9531f"/></svg>
    <span class="page-tab__num">2</span>
    <h2 class="slide-title">OUR TEAM</h2>
    <div class="team">
      <article class="member">
        <div class="member__photo" role="img" aria-label="Team member portrait placeholder"></div>
        <h3 class="member__name">NAME</h3>
        <p class="member__bio">Lorem Ipsum is simply dummy text of the printing and typesetting industry. Lorem Ipsum has been the industry's standard dummy text ever since the 1500s, when an unknown printer took a galley of type and scrambled it to make a type specimen book.</p>
      </article>
      <article class="member">
        <div class="member__photo" role="img" aria-label="Team member portrait placeholder"></div>
        <h3 class="member__name">NAME</h3>
        <p class="member__bio">Lorem Ipsum is simply dummy text of the printing and typesetting industry. Lorem Ipsum has been the industry's standard dummy text ever since the 1500s, when an unknown printer took a galley of type and scrambled it to make a type specimen book.</p>
      </article>
      <article class="member">
        <div class="member__photo" role="img" aria-label="Team member portrait placeholder"></div>
        <h3 class="member__name">NAME</h3>
        <p class="member__bio">Lorem Ipsum is simply dummy text of the printing and typesetting industry. Lorem Ipsum has been the industry's standard dummy text ever since the 1500s, when an unknown printer took a galley of type and scrambled it to make a type specimen book.</p>
      </article>
      <article class="member">
        <div class="member__photo" role="img" aria-label="Team member portrait placeholder"></div>
        <h3 class="member__name">NAME</h3>
        <p class="member__bio">Lorem Ipsum is simply dummy text of the printing and typesetting industry. Lorem Ipsum has been the industry's standard dummy text ever since the 1500s, when an unknown printer took a galley of type and scrambled it to make a type specimen book.</p>
      </article>
    </div>
    <svg class="footer-band" width="543" height="18" viewBox="0 0 543 18" aria-hidden="true"><polygon points="114,0 543,0 543,18 104,18" fill="#c9531f"/></svg>
    <div class="brand brand--footer"><span class="brand__dot"></span><span class="brand__name">Academy of<br>Rapid Clinical<br>Practice</span></div>
    <span class="footer-url">www.arcp-academy.org</span>
  </section>

  <section class="slide slide--membership">
    <svg class="page-tab" width="60" height="14" viewBox="0 0 60 14" aria-hidden="true"><polygon points="0,0 60,0 52,14 0,14" fill="#eea534"/><polygon points="52,14 60,0 58,0 50,14" fill="#c9531f"/></svg>
    <span class="page-tab__num">3</span>
    <h2 class="slide-title" style="width:398px;">MEMBERSHIP</h2>
    <div class="member-types">
      <section class="member-type">
        <h3 class="member-type__head"><svg width="8" height="9" viewBox="0 0 8 9" aria-hidden="true"><circle cx="4" cy="2.2" r="2.2" fill="#1d1d1d"/><path d="M0 9 C0 5.5 8 5.5 8 9Z" fill="#1d1d1d"/></svg>PHYSICIANS</h3>
        <p class="member-type__text">Members may be allopathic or osteopathic physicians holding an active license to practice medicine in the United States or its territories or be actively serving as physicians in the United States Armed Forces. Members must have a significant interest in the practice, teaching or administration of rapid care medicine. Retired physicians - those who are no longer actively practicing and/or have voluntarily allowed their medical licenses to lapse - who have been active Members of ARCP may continue to hold active Membership in the organization.</p>
      </section>
      <section class="member-type">
        <h3 class="member-type__head"><svg width="9" height="8" viewBox="0 0 9 8" aria-hidden="true"><rect x="0" y="2" width="9" height="6" fill="#1d1d1d"/><rect x="3" y="0" width="3" height="2.5" fill="none" stroke="#1d1d1d"/><rect x="4" y="3.5" width="1" height="3" fill="#fff"/><rect x="3" y="4.5" width="3" height="1" fill="#fff"/></svg>PHYSICIAN ASSISTANTS</h3>
        <p class="member-type__text">Members must hold an active license to practice medicine in the United States or its territories or be actively serving as physician assistants in the United States Armed Forces. Members must have a significant interest in the practice, teaching or administration of rapid care medicine.</p>
      </section>
      <section class="member-type">
        <h3 class="member-type__head"><svg width="8" height="9" viewBox="0 0 8 9" aria-hidden="true"><rect x="1" y="0" width="6" height="1.6" fill="#1d1d1d"/><circle cx="4" cy="3.2" r="1.8" fill="#1d1d1d"/><path d="M0 9 C0 5.8 8 5.8 8 9Z" fill="#1d1d1d"/></svg>NURSE PRACTITIONERS</h3>
        <p class="member-type__text">Members must hold an active license to practice medicine in the United States or its territories or be actively serving as nurse practitioner in the United States Armed Forces. Members must have a significant interest in the practice, teaching or administration of rapid care medicine.</p>
      </section>
      <section class="member-type">
        <h3 class="member-type__head"><svg width="10" height="8" viewBox="0 0 10 8" aria-hidden="true"><path d="M0.5 0 V7.5 H10" fill="none" stroke="#1d1d1d"/><path d="M2 6 L4.5 3 L6 4.5 L9 1.5" fill="none" stroke="#1d1d1d" stroke-width="1.1"/></svg>BENEFITS</h3>
        <p class="member-type__text">Members of ARCP will receive our monthly newsletter, Rapid Notes and the Journal of Rapid Clinical Practice as part of their membership, as well as reduced fees for annual conventions and conferences and preferred vendor relationships and rates. ARCP members can participate in many free or reduced-fee webinars and other educational activities. Members have free website access to clinical resources like consensus statements and practice guidelines. Finally, through the national voice given by ARCP, members will help direct the future of the specialty.</p>
      </section>
    </div>
    <div class="membership-photo" role="img" aria-label="Photo of two clinicians reviewing a patient chart together"></div>
    <svg class="footer-band" width="543" height="18" viewBox="0 0 543 18" aria-hidden="true"><polygon points="104,0 543,0 543,18 94,18" fill="#c9531f"/></svg>
    <div class="brand brand--footer"><span class="brand__dot"></span><span class="brand__name">Academy of<br>Rapid Clinical<br>Practice</span></div>
    <span class="footer-url">www.arcp-academy.org</span>
  </section>

</main>
</body>
</html>
```